Business Card Design

We need a basic, but modern design card. Our business is a local Queanbeyan/Canberra courier service, but can organise interstate delivery if needed. Our fleet ranges from 1 tonne vans to 8 tonne trucks.

Industry/Entity Type

Business

Contact Information for Business Card

Harbourline Freight
14 Tarrant Road
Marlow Vale NSW 2741

Owen Prescott
CEO

Phone: 02 61847315
Fax: 02 61847398
email: owen@harbourlinefreight.com.au

```html
<!DOCTYPE html>
<html lang="en">
<head>
<meta charset="utf-8">
<title>Harbourline Freight – Business Card</title>
<link href="https://fonts.googleapis.com/css2?family=Arimo:wght@400;700&display=swap" rel="stylesheet">
<style>
  :root {
    --page: #f2f2f2;
    --card: #ffffff;
    --ink: #2b2b2b;
    --brand-blue: #1d4f9c;
    --brand-orange: #e8591f;
    --frame-dark: #2a2a2a;
    --night-light: #a9b7e6;
    --night-mid: #4d5fa8;
    --night-deep: #161d42;
  }
  * { margin: 0; padding: 0; box-sizing: border-box; }
  html, body {
    width: 1200px; height: 816px; overflow: hidden;
    background: var(--page);
    font-family: "Arimo", Arial, sans-serif;
  }
  .card {
    position: absolute; left: 138px; top: 128px;
    width: 908px; height: 560px;
    background: var(--card);
    overflow: hidden;
  }
  .contact { position: absolute; left: 0; top: 0; color: var(--ink); }
  .contact__name {
    position: absolute; left: 84px; top: 42px; white-space: nowrap;
    font-size: 25px; font-weight: 700;
  }
  .contact__role {
    position: absolute; left: 84px; top: 72px;
    font-size: 22px; font-weight: 400;
  }
  .contact__row {
    position: absolute; left: 55px; height: 28px; white-space: nowrap;
    display: flex; align-items: center; gap: 9px;
    font-size: 22px;
  }
  .contact__row svg { width: 20px; height: 20px; flex: none; }
  .row-phone { top: 108px; }
  .row-fax { top: 143px; }
  .row-email { top: 179px; }
  .row-address { top: 214px; }

  .brand {
    position: absolute; left: 548px; top: 48px; width: 316px;
    text-align: center; color: var(--brand-blue);
    font-size: 38px; font-weight: 700; line-height: 1.1;
    text-transform: uppercase; letter-spacing: 0.5px;
    white-space: nowrap;
  }

  .web-band {
    position: absolute; left: 0; top: 258px; width: 100%; height: 38px;
    background: var(--brand-orange);
    color: #fff; font-size: 24px; font-weight: 700;
    padding-left: 88px; line-height: 38px;
  }
  .photo-frame {
    position: absolute; left: 0; top: 296px; width: 100%; height: 264px;
    background: var(--frame-dark);
  }
  .photo-frame__image {
    position: absolute; left: 17px; top: 2px; width: 874px; height: 248px;
    background:
      radial-gradient(ellipse 30% 45% at 62% 65%, rgba(200,215,255,0.35), transparent 70%),
      linear-gradient(100deg, var(--night-light) 0%, var(--night-mid) 45%, var(--night-deep) 100%);
  }
</style>
</head>
<body>
  <div class="card">
    <div class="contact">
      <div class="contact__name">Owen Prescott</div>
      <div class="contact__role">CEO</div>
      <div class="contact__row row-phone">
        <svg viewBox="0 0 20 20"><path d="M5 2c1 0 2 3 2 4s-2 1-1 3 3 5 5 6 2-1 3-1 4 1 4 2-2 3-4 3C8 19 1 12 1 6c0-2 3-4 4-4z" fill="var(--brand-orange)"/></svg>
        <span>02 61847315</span>
      </div>
      <div class="contact__row row-fax">
        <svg viewBox="0 0 20 20" fill="none" stroke="var(--brand-orange)" stroke-width="1.8"><rect x="5" y="2" width="10" height="5"/><rect x="2" y="7" width="16" height="8" rx="1"/><rect x="5" y="12" width="10" height="6" fill="#fff"/></svg>
        <span>02 61847398</span>
      </div>
      <div class="contact__row row-email">
        <svg viewBox="0 0 20 20" fill="none" stroke="var(--brand-orange)" stroke-width="1.8"><rect x="2" y="4" width="16" height="12"/><path d="M2 4l8 7 8-7"/></svg>
        <span>owen@harbourlinefreight.com.au</span>
      </div>
      <div class="contact__row row-address">
        <svg viewBox="0 0 20 20" fill="var(--brand-orange)"><path d="M10 1l9 7H1z"/><rect x="3" y="9" width="14" height="10"/><rect x="8" y="12" width="4" height="7" fill="#fff"/></svg>
        <span>14 Tarrant Road Marlow Vale NSW 2741</span>
      </div>
    </div>

    <div class="brand">Harbourline<br>Freight</div>

    <div class="web-band">www.harbourlinefreight.com.au</div>
    <div class="photo-frame">
      <div class="photo-frame__image" role="img" aria-label="Photo of a semi-trailer truck with headlights on, driving along a mountain road at dusk"></div>
    </div>
  </div>
</body>
</html>
```